Natural Dog Treat Box Label

We're looking for a modern, eye-catching label for our Natural Dog Treat Box. The design should clearly communicate the contents of the box, appealing to customers and highlighting the natural, wholesome ingredients inside

Brand Name: Merry Paws
Label Size: 210 mm x 148 mm Landscape
EAN Barcode: 5031847260591

Merry Paws Natural Treat Box for Dogs

Treat your dog to the ultimate natural snack experience with our Merry Paws Natural Treat Box. Packed with a variety of high-quality, single-ingredient chews, this box is designed to satisfy your dog's instincts while promoting dental health and overall well-being. Each treat is carefully sourced and free from artificial additives, offering your pet a wholesome and delicious indulgence.

Contents:
Chicken Feet (100g): A natural source of protein and collagen to support joint health.
Duck Feet (100g): Rich in nutrients and perfect for strong teeth and gums.
Beef Trachea (100g): Great for satisfying chewing while helping to clean teeth and promote healthy digestion.
Pork Bites (100g): Tasty, protein-packed bites your dog will love.
Chicken Necks (100g): A crunchy, flavorful treat that’s high in calcium and great for teeth cleaning.
Rabbit Ears (100g): A lean, hypoallergenic treat that’s gentle on sensitive stomachs.
Pig Ears (x2): A long-lasting chew that helps keep your dog entertained and satisfied.
Ideal for dogs of all sizes, the Merry Paws Natural Treat Box offers a variety of textures and flavors to keep your dog engaged and happy. Whether you're looking to reward your dog, support their health, or just give them a tasty treat, this box has something they'll love!

Preferably Natural Colours

Target Market(s)

Dog Owners

Industry/Entity Type

Pet Supplies

Requirements
Nice to have
• Product Contents Icons

```html
<!DOCTYPE html>
<html lang="en">
<head>
<meta charset="utf-8">
<title>Merry Paws Natural Treat Box Label</title>
<link rel="stylesheet" href="https://fonts.googleapis.com/css2?family=Arimo:wght@400;700&family=Luckiest+Guy&family=Source+Sans+3:wght@400&display=swap">
<style>
  :root {
    --sky: #5ecbee;
    --ink: #111111;
    --paper: #ffffff;
  }
  * { margin: 0; padding: 0; box-sizing: border-box; }
  html, body { width: 1200px; height: 1200px; overflow: hidden; background: var(--paper); }
  .canvas { position: relative; width: 1200px; height: 1200px; overflow: hidden; background: var(--paper); }

  .size-note {
    position: absolute; top: 118px; left: 0; width: 1240px; text-align: center;
    font-family: "Source Sans 3", sans-serif; font-size: 21px; color: var(--ink);
  }

  .label {
    position: absolute; left: 42px; top: 176px; width: 1146px; height: 808px;
    background: var(--sky);
  }
  .label-inner {
    position: absolute; left: 55px; top: 55px; width: 1036px; height: 698px;
    background: var(--paper);
  }

  .brand {
    position: absolute; left: 406px; top: 50px;
    display: flex; align-items: center; gap: 14px;
  }
  .brand-square { width: 77px; height: 77px; background: var(--sky); }
  .brand-name {
    font-family: "Arimo", sans-serif; font-weight: 700; font-size: 36px;
    color: var(--sky); line-height: 42px; text-transform: uppercase;
  }

  .title { position: absolute; left: 0; top: 0; width: 1200px; height: 1200px; pointer-events: none; }
  .title text {
    font-family: "Luckiest Guy", "Arial Black", sans-serif; font-size: 80px; font-weight: 900;
    fill: var(--paper); stroke: var(--sky); stroke-width: 8px; paint-order: stroke;
    stroke-linejoin: round;
  }

  .contents {
    position: absolute; left: 77px; top: 345px; width: 895px; height: 249px;
    border: 7px solid var(--sky); outline: 1px solid var(--sky); outline-offset: -11px;
    padding: 15px 0 0 15px;
    font-family: "Arimo", sans-serif; font-size: 16.4px; color: var(--ink);
    line-height: 26px; letter-spacing: -0.2px;
  }
  .contents-heading, .item-name { color: var(--sky); font-weight: 700; }

  .blurb {
    position: absolute; left: 20px; top: 603px; width: 996px; text-align: center;
    font-family: "Arimo", sans-serif; font-size: 16.4px; line-height: 22px;
    color: var(--ink); letter-spacing: -0.2px;
  }
</style>
</head>
<body>
<div class="canvas">
  <p class="size-note">210 mm x 148 mm Landscape</p>

  <div class="label" role="img" aria-label="Blue border decorated with a pattern of white paw prints">
    <div class="label-inner">
      <div class="brand">
        <span class="brand-square"></span>
        <span class="brand-name">Merry<br>Paws</span>
      </div>

      <div class="contents">
        <p class="contents-heading">Contents:</p>
        <p><span class="item-name">Chicken Feet (100g):</span> A natural source of protein and collagen to support joint health.</p>
        <p><span class="item-name">Duck Feet (100g):</span> Rich in nutrients and perfect for strong teeth and gums.</p>
        <p><span class="item-name">Beef Trachea (100g):</span> Great for satisfying chewing while helping to clean teeth and promote healthy digestion.</p>
        <p><span class="item-name">Pork Bites (100g):</span> Tasty, protein-packed bites your dog will love.</p>
        <p><span class="item-name">Chicken Necks (100g):</span> A crunchy, flavorful treat that’s high in calcium and great for teeth cleaning.</p>
        <p><span class="item-name">Rabbit Ears (100g):</span> A lean, hypoallergenic treat that’s gentle on sensitive stomachs.</p>
        <p><span class="item-name">Pig Ears (x2):</span> A long-lasting chew that helps keep your dog entertained and satisfied.</p>
      </div>

      <p class="blurb">Ideal for dogs of all sizes, the Merry Paws Natural Treat Box offers a variety of textures and flavors to keep your dog engaged<br>and happy. Whether you're looking to reward your dog, support their health, or just give them a tasty treat,<br>this box has something they'll love!</p>
    </div>
  </div>

  <svg class="title" viewBox="0 0 1200 1200" aria-label="Natural Treat Box for Dogs">
    <defs>
      <path id="arc-top" d="M315,410 Q610,537 905,395"/>
      <path id="arc-bottom" d="M305,498 Q612,612 922,492"/>
    </defs>
    <text><textPath href="#arc-top" startOffset="50%" text-anchor="middle" textLength="590" lengthAdjust="spacingAndGlyphs">NATURAL TREAT</textPath></text>
    <text><textPath href="#arc-bottom" startOffset="50%" text-anchor="middle" textLength="630" lengthAdjust="spacingAndGlyphs">BOX FOR DOGS</textPath></text>
  </svg>
</div>
</body>
</html>
```